Real Estate Website

We have a an existing website - harborkeyhomes.com.au which we want redesigned.

We want it to look more like the design/style of https://www.stallworth.com.au/

```html
<!DOCTYPE html>
<html lang="en">
<head>
<meta charset="utf-8">
<title>Harborkey Homes</title>
<link href="https://fonts.googleapis.com/css2?family=Montserrat:wght@300;400;500;600;700&family=Oswald:wght@500&display=swap" rel="stylesheet">
<style>
:root{
  --navy:#0b2043;
  --teal:#00878f;
  --teal-dark:#006f76;
  --ink:#222b33;
  --muted:#555e66;
  --line:#d7dde2;
  --pale:#f2f6f8;
  --star:#f5a623;
  --white:#ffffff;
}
*{box-sizing:border-box;margin:0;padding:0}
html,body{width:1200px;height:4213px;overflow:hidden}
body{font-family:'Montserrat',sans-serif;color:var(--ink);background:var(--white);position:relative}
section,header,footer{position:absolute;left:0;width:1200px}
.abs{position:absolute}

/* header */
.site-header{top:0;height:72px;background:var(--navy)}
.brand{left:140px;top:22px;color:var(--white);font-size:22px;font-weight:400;letter-spacing:3px}
.nav{left:479px;top:27px;display:flex;gap:18px;font-size:11.5px;color:var(--white);font-weight:500}
.nav-cta{left:812px;top:18px;width:110px;height:35px;background:var(--teal);color:var(--white);font-size:11.5px;font-weight:600;display:flex;align-items:center;justify-content:center}
.header-phone{left:934px;top:24px;display:flex;align-items:center;gap:8px;color:var(--white);font-weight:600;font-size:14px}

/* hero */
.hero{top:72px;height:538px;background:linear-gradient(100deg,#c9c2b6 0%,#e8e4dd 40%,#d8d2c8 70%,#b7a895 100%)}
.hero-panel{left:140px;top:145px;width:460px;height:248px;background:var(--teal);border-left:4px solid rgba(255,255,255,.25)}
.hero-panel h1{position:absolute;left:36px;top:60px;font-family:'Oswald',sans-serif;font-weight:500;color:var(--white);font-size:22px;line-height:38px}
.hero-panel h1 span{font-size:29px}
.btn-outline{position:absolute;left:36px;top:145px;width:130px;height:40px;background:var(--white);color:var(--teal);font-size:11.5px;font-weight:600;display:flex;align-items:center;justify-content:center}

/* features */
.features{top:610px;height:718px}
.feature{position:absolute;width:213px;height:258px;border:1px solid var(--line);text-align:center}
.feature-icon{width:102px;height:102px;border-radius:50%;border:2px solid var(--teal);margin:24px auto 0;display:flex;align-items:center;justify-content:center}
.feature-icon div{width:70px;height:70px;border-radius:50%;background:linear-gradient(135deg,#1f8c93,#25465f)}
.feature h3{color:var(--teal);font-size:12.5px;font-weight:600;margin-top:22px;line-height:17px;padding:0 20px}
.feature p{font-size:11px;color:var(--muted);margin-top:6px;line-height:15px;padding:0 24px}

/* testimonial */
.testimonials{top:1328px;height:482px;background:linear-gradient(90deg,#2b2926,#3a3834 50%,#2a2825);text-align:center;color:var(--white)}
.testimonials h2{position:absolute;top:78px;width:100%;font-size:28px;font-weight:500}
.avatar{position:absolute;left:545px;top:147px;width:106px;height:106px;border-radius:50%;background:linear-gradient(160deg,#c9d4dc,#8a9aa6);border:3px solid rgba(255,255,255,.5)}
.quote{position:absolute;left:160px;top:272px;width:880px;font-size:11.2px;line-height:23px}
.stars{position:absolute;top:355px;width:100%;display:flex;justify-content:center;gap:5px}
.client{position:absolute;top:386px;width:100%;font-size:12px;font-weight:500}
.arrow{position:absolute}

/* featured listing */
.featured{top:1810px;height:572px}
.section-title{position:absolute;width:100%;text-align:center;font-size:29px;font-weight:500;color:var(--ink)}
.section-title em{font-style:normal;color:var(--teal)}
.listing{position:absolute;top:142px;width:293px;height:345px;border:1px solid var(--line);text-align:center}
.listing-tag{height:48px;background:var(--teal);color:var(--white);font-size:13px;font-weight:600;display:flex;align-items:center;justify-content:center;margin:-1px -1px 0}
.listing-photo{margin:8px 7px 0;height:207px;background:linear-gradient(160deg,#e9e6e0,#b9b1a5 60%,#6f6a62)}
.listing h3{color:var(--teal);font-size:12.5px;font-weight:600;margin-top:22px}
.listing p{font-size:11px;color:var(--muted);margin-top:10px}

/* cta */
.check{top:2382px;height:321px;background:var(--teal);text-align:center;color:var(--white)}
.check h2{position:absolute;top:78px;width:100%;font-size:32px;font-weight:500;line-height:42px}
.check-form{position:absolute;left:244px;top:183px;width:712px;height:52px;background:var(--white);display:flex;align-items:center;padding:0 5px 0 24px}
.check-form span{flex:1;text-align:left;color:#6b737a;font-size:13px}
.check-form b{width:160px;height:42px;background:var(--teal);color:var(--white);font-size:12.5px;font-weight:600;display:flex;align-items:center;justify-content:center}

/* news & sales */
.updates{top:2703px;height:632px}
.col-title{position:absolute;top:84px;font-size:23px;font-weight:500}
.col-title em{font-style:normal;color:var(--teal)}
.view-all{position:absolute;top:92px;font-size:11px;font-weight:600;color:var(--teal);text-decoration:underline}
.news-photo{position:absolute;width:195px;height:190px}
.news-card{position:absolute;width:266px;background:var(--white);box-shadow:0 4px 18px rgba(0,0,0,.12);padding:22px 18px}
.news-date{display:flex;align-items:center;gap:7px;font-size:11.5px;font-weight:500}
.news-card h4{font-size:11px;font-weight:600;line-height:18px;margin-top:9px}
.btn-teal{display:inline-flex;width:100px;height:35px;background:var(--teal);color:var(--white);font-size:10.5px;font-weight:600;align-items:center;justify-content:center;margin-top:8px}
.sale{position:absolute;left:631px;width:428px;height:116px;background:var(--white);box-shadow:0 4px 18px rgba(0,0,0,.1)}
.sale-photo{position:absolute;left:0;top:0;width:131px;height:116px;background:linear-gradient(150deg,#eae7e2,#b1a89c 60%,#5b5650)}
.sale-price{position:absolute;left:8px;top:0;background:var(--teal);color:var(--white);font-size:10px;font-weight:600;padding:4px 9px}
.sale-body{position:absolute;left:146px;top:22px;width:265px}
.sale-body h4{font-size:11px;font-weight:600;line-height:17px}
.sale-body p{font-size:10.5px;color:var(--muted);line-height:19px;margin-top:4px}

/* agents */
.agents{top:3335px;height:462px;background:var(--pale)}
.agent{position:absolute;top:144px;width:213px;height:233px;background:var(--white);border:1px solid var(--line);text-align:center}
.agent-photo{width:102px;height:102px;border-radius:50%;margin:23px auto 0;background:linear-gradient(160deg,#dfe4e8,#8d99a3)}
.agent h3{color:var(--teal);font-size:17px;font-weight:500;margin-top:13px}
.agent .role{font-size:12px;color:var(--muted);margin-top:4px}
.agent-contact{display:flex;justify-content:center;gap:14px;margin-top:18px;font-size:12px;font-weight:500}
.agent-contact span{display:flex;align-items:center;gap:4px}

/* footer */
.site-footer{top:3797px;height:369px;background:var(--navy);color:var(--white)}
.foot-col{position:absolute;top:72px}
.foot-col h5{font-size:14.5px;font-weight:600;margin-bottom:16px}
.foot-col li{list-style:none;font-size:11px;line-height:25.4px}
.contact-item{display:flex;gap:12px;font-size:11px;line-height:17px;margin-bottom:14px}
.contact-item b{font-weight:600;display:block}
.bottom-bar{left:0;top:4166px;width:1200px;height:47px;background:var(--teal);color:var(--white)}
.copyright{left:142px;top:17px;font-size:10.5px}
.social{top:9px;width:30px;height:30px;border:1.5px solid var(--white);border-radius:50%}
</style>
</head>
<body>

<header class="site-header">
  <div class="abs brand">HARBORKEY HOMES</div>
  <nav class="abs nav"><span>BUYING</span><span>SELLING</span><span>RENTING</span><span>BLOG</span><span>ABOUT US</span></nav>
  <div class="abs nav-cta">CONTACT US</div>
  <div class="abs header-phone">
    <svg width="20" height="20" viewBox="0 0 20 20"><circle cx="10" cy="10" r="10" fill="#fff"/><path d="M7 5.5l1.6 2.2-1 1.2c.6 1.3 1.5 2.2 2.8 2.8l1.2-1 2.2 1.6-.8 1.7c-3.6-.2-6.5-3.1-6.7-6.7z" fill="#0b2043"/></svg>
    555.014.2290
  </div>
</header>

<section class="hero" role="img" aria-label="Photo of a couple viewing a bright empty home with large windows">
  <div class="abs hero-panel">
    <h1>WE WANT TO BE<br><span>"YOUR FRIEND IN REAL ESTATE!"</span></h1>
    <div class="btn-outline">CONTACT US</div>
  </div>
</section>

<section class="features">
  <div class="feature" style="left:142px;top:85px"><div class="feature-icon"><div role="img" aria-label="Icon of a hand holding a house"></div></div><h3>Low, All Inclusive Fees</h3><p>Simple and fair</p></div>
  <div class="feature" style="left:376px;top:85px"><div class="feature-icon"><div role="img" aria-label="Icon of a team of people"></div></div><h3>Team of Local Experts</h3><p>Advice and service on-call</p></div>
  <div class="feature" style="left:610px;top:85px"><div class="feature-icon"><div role="img" aria-label="Icon of a hand tapping houses"></div></div><h3>Technology To Make Life Easier</h3><p>Information and updates at your fingertips</p></div>
  <div class="feature" style="left:844px;top:85px"><div class="feature-icon"><div role="img" aria-label="Icon of a house"></div></div><h3>3D Virtual Inspections</h3><p>Check in on your property in 3D</p></div>
  <div class="feature" style="left:142px;top:373px"><div class="feature-icon"><div role="img" aria-label="Icon of a home with tenants"></div></div><h3>Quality Tenants</h3><p>Comprehensively screened and vetted</p></div>
  <div class="feature" style="left:376px;top:373px"><div class="feature-icon"><div role="img" aria-label="Icon of a handshake"></div></div><h3>Faster Leasing</h3><p>Improving your investment returns</p></div>
  <div class="feature" style="left:610px;top:373px"><div class="feature-icon"><div role="img" aria-label="Icon of hands exchanging money"></div></div><h3>Daily Rental Payments</h3><p>No more waiting till end of the month!</p></div>
  <div class="feature" style="left:844px;top:373px"><div class="feature-icon"><div role="img" aria-label="Icon of a house with a maintenance mark"></div></div><h3>Professional Maintenance</h3><p>Lowest cost and quality guaranteed</p></div>
</section>

<section class="testimonials" role="img" aria-label="Dimmed photo of a styled living room">
  <h2>WHAT OUR CLIENTS SAY</h2>
  <div class="avatar" role="img" aria-label="Portrait of the agent"></div>
  <p class="quote">Martin and I would like to say a huge thank you for all your hard work. Daniel, you have always been VERY PROFESSIONAL in your approach towards us and the clients. Your enthusiasm to take on our 'project' was always present. We loved that from you. We knew at all times that, Yes we were with the best real estate agent and we had the best agent to help us with this 'big move'. Once again many thanks.</p>
  <div class="stars">
    <svg width="18" height="18" viewBox="0 0 20 20"><path d="M10 1l2.7 5.8 6.3.7-4.7 4.3 1.3 6.2L10 14.9 4.4 18l1.3-6.2L1 7.5l6.3-.7z" fill="var(--star)"/></svg>
    <svg width="18" height="18" viewBox="0 0 20 20"><path d="M10 1l2.7 5.8 6.3.7-4.7 4.3 1.3 6.2L10 14.9 4.4 18l1.3-6.2L1 7.5l6.3-.7z" fill="var(--star)"/></svg>
    <svg width="18" height="18" viewBox="0 0 20 20"><path d="M10 1l2.7 5.8 6.3.7-4.7 4.3 1.3 6.2L10 14.9 4.4 18l1.3-6.2L1 7.5l6.3-.7z" fill="var(--star)"/></svg>
    <svg width="18" height="18" viewBox="0 0 20 20"><path d="M10 1l2.7 5.8 6.3.7-4.7 4.3 1.3 6.2L10 14.9 4.4 18l1.3-6.2L1 7.5l6.3-.7z" fill="var(--star)"/></svg>
    <svg width="18" height="18" viewBox="0 0 20 20"><path d="M10 1l2.7 5.8 6.3.7-4.7 4.3 1.3 6.2L10 14.9 4.4 18l1.3-6.2L1 7.5l6.3-.7z" fill="var(--star)"/></svg>
  </div>
  <div class="client">Sophie &amp; Martin Delacroix</div>
  <svg class="arrow" style="left:98px;top:292px" width="14" height="26" viewBox="0 0 14 26"><path d="M12 2L2 13l10 11" stroke="#fff" stroke-width="2" fill="none"/></svg>
  <svg class="arrow" style="left:1088px;top:292px" width="14" height="26" viewBox="0 0 14 26"><path d="M2 2l10 11L2 24" stroke="#fff" stroke-width="2" fill="none"/></svg>
</section>

<section class="featured">
  <h2 class="section-title" style="top:76px">FEATURED <em>LISTING</em></h2>
  <div class="listing" style="left:141px"><div class="listing-tag">DEPOSIT TAKEN !!!</div><div class="listing-photo" role="img" aria-label="Photo of a bright apartment living room"></div><h3>Modern Designer Apartment.</h3><p>D12/8 Larkin Street For Rent In Cove</p></div>
  <div class="listing" style="left:453px"><div class="listing-tag">FOR SALE $749,000</div><div class="listing-photo" role="img" aria-label="Photo of an apartment lounge and dining area"></div><h3>Modern Apartment!!</h3><p>504/16 Tarrant Street For Sale in Fernvale</p></div>
  <div class="listing" style="left:765px"><div class="listing-tag">DEPOSIT TAKEN !!!</div><div class="listing-photo" role="img" aria-label="Photo of a tiled living room with sofa"></div><h3>Villa Style Apartment – Gas All Inclusive</h3><p>3/210 Ocean Parade For Rent In Bayridge</p></div>
  <svg class="arrow" style="left:98px;top:300px" width="14" height="26" viewBox="0 0 14 26"><path d="M12 2L2 13l10 11" stroke="#333" stroke-width="1.6" fill="none"/></svg>
  <svg class="arrow" style="left:1088px;top:300px" width="14" height="26" viewBox="0 0 14 26"><path d="M2 2l10 11L2 24" stroke="#333" stroke-width="1.6" fill="none"/></svg>
</section>

<section class="check">
  <h2>CHECK TO SEE IF YOUR PROPERTY<br>IS ELIGIBLE FOR THE PROPPER SEVICE</h2>
  <div class="check-form"><span>Enter Your Post Code To Check Your Service Area</span><b>CHECK LOCATION</b></div>
</section>

<section class="updates">
  <h2 class="col-title" style="left:142px">LATEST <em>NEWS</em></h2>
  <span class="view-all" style="left:502px">VIEW ALL</span>
  <div class="news-photo" style="left:142px;top:139px;background:linear-gradient(160deg,#e7ded0,#c0392b 55%,#7a2a20)" role="img" aria-label="Photo of a price reduced for sale sign"></div>
  <div class="news-card" style="left:301px;top:158px"><div class="news-date"><svg width="13" height="13" viewBox="0 0 13 13"><rect x="1" y="2" width="11" height="10" fill="none" stroke="var(--teal)" stroke-width="1.3"/><path d="M1 5h11" stroke="var(--teal)" stroke-width="1.3"/></svg>17/01/2019</div><h4>FIRST HOME BUYERS GUIDE – WHAT TO LOOK FOR</h4><span class="btn-teal">READ MORE</span></div>
  <div class="news-photo" style="left:142px;top:359px;background:linear-gradient(180deg,#cfe0ef,#d9cbb5 50%,#7aa04a)" role="img" aria-label="Photo of a two storey house with lawn"></div>
  <div class="news-card" style="left:301px;top:376px"><div class="news-date"><svg width="13" height="13" viewBox="0 0 13 13"><rect x="1" y="2" width="11" height="10" fill="none" stroke="var(--teal)" stroke-width="1.3"/><path d="M1 5h11" stroke="var(--teal)" stroke-width="1.3"/></svg>21/03/2017</div><h4>38 WEXFORD PARADE, ELMHURST – AUCTION DAY</h4><span class="btn-teal">READ MORE</span></div>

  <h2 class="col-title" style="left:631px">RECENT <em>SALES</em></h2>
  <span class="view-all" style="left:993px">VIEW ALL</span>
  <div class="sale" style="top:139px"><div class="sale-photo" role="img" aria-label="Photo of an apartment interior"></div><span class="sale-price">$670,000</span><div class="sale-body"><h4>Sold by Renee Carter 0400 555 206</h4><p>Lorem ipsum dolor sit amet onsectetuer adipiscing elit, sed diam nonummy nibh euismod tincidunt ut laoreet</p></div></div>
  <div class="sale" style="top:284px"><div class="sale-photo" role="img" aria-label="Photo of an apartment living area"></div><span class="sale-price">$609,000</span><div class="sale-body"><h4>Modern Apartment close to all Amenities</h4><p>Lorem ipsum dolor sit amet onsectetuer adipiscing elit, sed diam nonummy nibh euismod tincidunt ut laoreet</p></div></div>
  <div class="sale" style="top:430px"><div class="sale-photo" role="img" aria-label="Photo of a furnished apartment"></div><span class="sale-price">$500,000</span><div class="sale-body" style="top:12px"><h4>Great apartment for Investment or First Home!</h4><p>Lorem ipsum dolor sit amet onsectetuer adipiscing elit, sed diam nonummy nibh euismod tincidunt ut laoreet</p></div></div>
</section>

<section class="agents">
  <h2 class="section-title" style="top:82px">OUR <em>AGENTS</em></h2>
  <div class="agent" style="left:142px"><div class="agent-photo" role="img" aria-label="Portrait of agent"></div><h3>Kai Nguyen</h3><div class="role">Director</div><div class="agent-contact"><span><svg width="11" height="11" viewBox="0 0 20 20"><path d="M4 2l4 5-2 2.5c1.3 2.7 3.3 4.7 6 6L14.5 13l5 4-2 3C9.5 19.5.5 10.5 0 4z" fill="var(--teal)"/></svg>0400 555 038</span><span><svg width="12" height="10" viewBox="0 0 12 10"><rect width="12" height="10" fill="var(--teal)"/><path d="M0 0l6 5 6-5" stroke="#fff" fill="none"/></svg>Contact</span></div></div>
  <div class="agent" style="left:376px"><div class="agent-photo" role="img" aria-label="Portrait of agent"></div><h3>Daniel Lau</h3><div class="role">Principal</div><div class="agent-contact"><span><svg width="11" height="11" viewBox="0 0 20 20"><path d="M4 2l4 5-2 2.5c1.3 2.7 3.3 4.7 6 6L14.5 13l5 4-2 3C9.5 19.5.5 10.5 0 4z" fill="var(--teal)"/></svg>0400555762</span><span><svg width="12" height="10" viewBox="0 0 12 10"><rect width="12" height="10" fill="var(--teal)"/><path d="M0 0l6 5 6-5" stroke="#fff" fill="none"/></svg>Contact</span></div></div>
  <div class="agent" style="left:610px"><div class="agent-photo" role="img" aria-label="Portrait of agent"></div><h3>Talia Moana</h3><div class="role">Property Management</div><div class="agent-contact"><span><svg width="11" height="11" viewBox="0 0 20 20"><path d="M4 2l4 5-2 2.5c1.3 2.7 3.3 4.7 6 6L14.5 13l5 4-2 3C9.5 19.5.5 10.5 0 4z" fill="var(--teal)"/></svg>0400 555 255</span><span><svg width="12" height="10" viewBox="0 0 12 10"><rect width="12" height="10" fill="var(--teal)"/><path d="M0 0l6 5 6-5" stroke="#fff" fill="none"/></svg>Contact</span></div></div>
  <div class="agent" style="left:844px"><div class="agent-photo" role="img" aria-label="Portrait of agent"></div><h3>Renee Carter</h3><div class="role">Sales Assistant</div><div class="agent-contact"><span><svg width="11" height="11" viewBox="0 0 20 20"><path d="M4 2l4 5-2 2.5c1.3 2.7 3.3 4.7 6 6L14.5 13l5 4-2 3C9.5 19.5.5 10.5 0 4z" fill="var(--teal)"/></svg>0400 555 206</span><span><svg width="12" height="10" viewBox="0 0 12 10"><rect width="12" height="10" fill="var(--teal)"/><path d="M0 0l6 5 6-5" stroke="#fff" fill="none"/></svg>Contact</span></div></div>
  <svg class="arrow" style="left:98px;top:250px" width="14" height="26" viewBox="0 0 14 26"><path d="M12 2L2 13l10 11" stroke="#333" stroke-width="1.6" fill="none"/></svg>
  <svg class="arrow" style="left:1088px;top:250px" width="14" height="26" viewBox="0 0 14 26"><path d="M2 2l10 11L2 24" stroke="#333" stroke-width="1.6" fill="none"/></svg>
</section>

<footer class="site-footer">
  <div class="foot-col" style="left:142px"><h5>BUYING</h5><ul><li>• Properties for Sale</li><li>• Commercial for Sale</li><li>• Land for Sale</li><li>• Open Homes</li><li>• Auction Timetable</li><li>• Buying Tips</li><li>• Sales Team</li><li>• Property Alert</li></ul></div>
  <div class="foot-col" style="left:368px"><h5>SELLING</h5><ul><li>• Selling Tips</li><li>• Market Appraisal</li><li>• Recent Sales</li><li>• Testimonials</li></ul></div>
  <div class="foot-col" style="left:579px"><h5>RENTING</h5><ul><li>• Properties for Lease</li><li>• Commercial for Lease</li><li>• Rental Open Homes</li><li>• Guide to Renting</li><li>• Lease Appraisal</li><li>• Property Management Team</li><li>• Leased Properties</li><li>• Property Alert</li></ul></div>
  <div class="foot-col" style="left:852px"><h5>CONTACT DETAILS</h5>
    <div class="contact-item"><svg width="12" height="14" viewBox="0 0 12 14"><path d="M6 0a5 5 0 015 5c0 4-5 9-5 9S1 9 1 5a5 5 0 015-5z" fill="var(--teal)"/><circle cx="6" cy="5" r="1.8" fill="var(--navy)"/></svg><div><b>Address</b>Shop 4, 88 Harbour Rd,<br>Eastport Nsw 2999</div></div>
    <div class="contact-item"><svg width="12" height="12" viewBox="0 0 20 20"><path d="M4 2l4 5-2 2.5c1.3 2.7 3.3 4.7 6 6L14.5 13l5 4-2 3C9.5 19.5.5 10.5 0 4z" fill="var(--teal)"/></svg><div><b>Phone</b>02 5550 1971</div></div>
    <div class="contact-item"><svg width="12" height="12" viewBox="0 0 20 20"><path d="M4 2l4 5-2 2.5c1.3 2.7 3.3 4.7 6 6L14.5 13l5 4-2 3C9.5 19.5.5 10.5 0 4z" fill="var(--teal)"/></svg><div><b>Fax</b>02 5550 1971</div></div>
    <div class="contact-item"><svg width="13" height="10" viewBox="0 0 12 10"><rect width="12" height="10" fill="var(--teal)"/><path d="M0 0l6 5 6-5" stroke="var(--navy)" fill="none"/></svg><div><b>Email</b>Enquiries@harborkeyhomes.com.au</div></div>
  </div>
</footer>

<div class="abs bottom-bar">
  <div class="abs copyright">© 2021 Harborkey Homes . All Rights Reserved</div>
  <div class="abs social" style="left:946px"></div>
  <div class="abs social" style="left:987px"></div>
  <div class="abs social" style="left:1028px"></div>
</div>

</body>
</html>
```